Stationery & Business Card Design Project

We require our stationary to be professional, which will stand out but also be sophisticated and reputable.

We also require the following:

* Business card must be double sided
* Logo must stand out with brightfund colours used. Other colours may be added but only in small doses as not to overtake the main colours.
* For business card brightfund pty ltd smsf specialists with administrators at bottom left on the front of the card and details on the back

Industry/Entity Type

Business

Requirements
Must have
• * Business Cards
* With compliments slips –2 different ones
* Forwarding mail slip (smaller version of a with compliments slip)

```html
<!DOCTYPE html>
<html lang="en">
<head>
<meta charset="utf-8">
<title>brightfund stationery</title>
<link rel="stylesheet" href="https://fonts.googleapis.com/css2?family=Source+Sans+3:wght@400;600;700&display=swap">
<style>
  :root {
    --navy: #1f2a6e;
    --navy-deep: #17205a;
    --royal: #2e3b94;
    --royal-light: #3f4ca6;
    --grey: #8a8c92;
    --grey-text: #6b6d73;
    --white: #ffffff;
    --backdrop: #000000;
  }
  * { margin: 0; padding: 0; box-sizing: border-box; }
  html, body { width: 900px; height: 1200px; overflow: hidden; background: var(--backdrop); }
  body { position: relative; font-family: "Source Sans 3", "Helvetica Neue", Arial, sans-serif; }

  .piece { position: absolute; overflow: hidden; }
  .piece > svg.backdrop { position: absolute; inset: 0; width: 100%; height: 100%; }

  .brand { position: absolute; display: flex; align-items: center; }
  .brand-square { background: var(--navy); flex: none; }
  .brand-words { display: flex; flex-direction: column; line-height: 1; }
  .brand-name { font-weight: 600; letter-spacing: -0.5px; }
  .brand-tag { font-weight: 600; letter-spacing: 2.5px; margin-top: 2px; }

  /* Business card front */
  .card-front { left: 35px; top: 77px; width: 354px; height: 215px; background: var(--white); }
  .card-front .brand { left: 61px; top: 31px; }
  .card-front .brand-square { width: 56px; height: 56px; margin-right: 8px; }
  .card-front .brand-name { font-size: 34px; color: var(--navy); }
  .card-front .brand-tag { font-size: 8px; color: var(--navy); }
  .holder { position: absolute; left: 22px; top: 130px; width: 140px; text-align: center; }
  .holder-name { font-size: 14px; font-weight: 700; color: var(--navy); }
  .holder-role { font-size: 11.5px; color: var(--grey-text); margin-top: 1px; }
  .card-divider { position: absolute; left: 172px; top: 124px; width: 1px; height: 60px; background: #c9cad0; }
  .contact-list { position: absolute; left: 180px; top: 122px; list-style: none; }
  .contact-list li { display: flex; align-items: center; font-size: 10px; color: var(--grey-text); height: 12.5px; }
  .contact-list svg { width: 9px; height: 9px; margin-right: 5px; fill: var(--navy); }

  /* Business card back */
  .card-back { left: 409px; top: 77px; width: 354px; height: 215px; }
  .card-back .brand { left: 68px; top: 77px; }
  .card-back .brand-square { width: 54px; height: 54px; margin-right: 8px; background: var(--grey); }
  .card-back .brand-name { font-size: 32px; color: var(--white); }
  .card-back .brand-tag { font-size: 7.5px; color: var(--white); }
  .card-back .web { position: absolute; left: 0; right: 0; bottom: 8px; text-align: center; font-size: 11px; font-weight: 700; letter-spacing: 0.8px; color: var(--white); }

  /* With compliments slip */
  .slip { left: 35px; top: 320px; width: 828px; height: 390px; background: var(--white); }
  .slip .brand { left: 31px; top: 30px; }
  .slip .brand-square { width: 68px; height: 68px; margin-right: 8px; }
  .slip .brand-name { font-size: 41px; color: var(--navy); }
  .slip .brand-tag { font-size: 9.5px; color: var(--navy); }
  .slip-divider { position: absolute; left: 312px; top: 32px; width: 1.5px; height: 66px; background: #b9bac0; }
  .slip-title { position: absolute; left: 340px; top: 50px; font-size: 26px; font-weight: 600; color: var(--navy); }
  .slip-title span { color: var(--grey-text); font-weight: 700; }
  .slip-address { position: absolute; left: 32px; top: 110px; font-size: 15px; color: var(--grey-text); }
  .slip .web { position: absolute; left: 23px; bottom: 10px; font-size: 14px; font-weight: 700; letter-spacing: 1px; color: var(--white); }

  /* Envelope */
  .envelope { left: 35px; top: 728px; width: 828px; height: 390px; }
  .envelope .brand { left: 221px; top: 140px; }
  .envelope .brand-square { width: 104px; height: 104px; margin-right: 12px; background: var(--grey); }
  .envelope .brand-name { font-size: 60px; color: var(--white); }
  .envelope .brand-tag { font-size: 13px; color: var(--white); letter-spacing: 4px; }
  .envelope-contacts { position: absolute; left: 0; right: 0; bottom: 16px; display: flex; justify-content: center; gap: 10px; list-style: none; }
  .envelope-contacts li { display: flex; align-items: center; font-size: 12px; color: var(--white); }
  .envelope-contacts svg { width: 11px; height: 11px; margin-right: 6px; fill: var(--white); }
</style>
</head>
<body>

<svg width="0" height="0" style="position:absolute">
  <defs>
    <symbol id="icon-pin" viewBox="0 0 10 10"><path d="M5 0a3.5 3.5 0 0 0-3.5 3.5C1.5 6 5 10 5 10s3.5-4 3.5-6.5A3.5 3.5 0 0 0 5 0zm0 5a1.4 1.4 0 1 1 0-2.8A1.4 1.4 0 0 1 5 5z"/></symbol>
    <symbol id="icon-mail" viewBox="0 0 10 10"><path d="M0 2h10v6H0zM1 3v.3l4 2.4 4-2.4V3zm0 1.5V7h8V4.5L5 6.9z" fill-rule="evenodd"/></symbol>
    <symbol id="icon-phone" viewBox="0 0 10 10"><path d="M2.2 0.5l1.6 2-0.9 1.2c0.6 1.3 1.5 2.2 2.8 2.8l1.2-0.9 2 1.6-1 2C4.6 9.2 0.8 5.4 0.2 1.5z"/></symbol>
    <symbol id="icon-globe" viewBox="0 0 10 10"><circle cx="5" cy="5" r="4.5"/><path d="M0.5 5h9M5 0.5v9" stroke="#fff" stroke-width="0.7"/></symbol>
    <linearGradient id="royal-fill" x1="0" y1="0" x2="1" y2="1">
      <stop offset="0" stop-color="#34409a"/>
      <stop offset="1" stop-color="#25307f"/>
    </linearGradient>
  </defs>
</svg>

<!-- Business card front -->
<section class="piece card-front">
  <svg class="backdrop" viewBox="0 0 354 215" preserveAspectRatio="none" aria-hidden="true">
    <path d="M0 168 Q170 200 354 198 L354 215 L0 215 Z" fill="var(--navy)"/>
    <path d="M0 162 Q170 194 354 193" fill="none" stroke="var(--grey)" stroke-width="5"/>
  </svg>
  <div class="brand">
    <div class="brand-square"></div>
    <div class="brand-words"><span class="brand-name">brightfund</span><span class="brand-tag">smsf specialists</span></div>
  </div>
  <div class="holder">
    <p class="holder-name">Clara Whitfield</p>
    <p class="holder-role">Independent Distributor</p>
  </div>
  <div class="card-divider"></div>
  <ul class="contact-list">
    <li><svg><use href="#icon-pin"/></svg>PO Box 318, Harbourview, NT 0870</li>
    <li><svg><use href="#icon-mail"/></svg>clara@brightfund.com.au</li>
    <li><svg><use href="#icon-phone"/></svg>0412 663 108</li>
    <li><svg><use href="#icon-phone"/></svg>1300 555 014</li>
    <li><svg><use href="#icon-globe"/></svg>www.brightfund.com.au</li>
  </ul>
</section>

<!-- Business card back -->
<section class="piece card-back">
  <svg class="backdrop" viewBox="0 0 354 215" preserveAspectRatio="none" aria-hidden="true">
    <rect width="354" height="215" fill="url(#royal-fill)"/>
    <path d="M0 0 H354 V40 Q200 -10 60 90 Q20 70 0 60 Z" fill="#ffffff" opacity="0.07"/>
  </svg>
  <div class="brand">
    <div class="brand-square"></div>
    <div class="brand-words"><span class="brand-name">brightfund</span><span class="brand-tag">smsf specialists</span></div>
  </div>
  <p class="web">www.brightfund.com.au</p>
</section>

<!-- With compliments slip -->
<section class="piece slip">
  <svg class="backdrop" viewBox="0 0 828 390" preserveAspectRatio="none" aria-hidden="true">
    <path d="M0 282 Q380 370 828 334 L828 390 L0 390 Z" fill="var(--navy-deep)"/>
    <path d="M0 272 Q380 362 828 324" fill="none" stroke="var(--grey)" stroke-width="10"/>
  </svg>
  <div class="brand">
    <div class="brand-square"></div>
    <div class="brand-words"><span class="brand-name">brightfund</span><span class="brand-tag">smsf specialists</span></div>
  </div>
  <div class="slip-divider"></div>
  <h1 class="slip-title">With <span>Compliments</span></h1>
  <p class="slip-address">PO Box 318, Harbourview, NT 0870</p>
  <p class="web">www.brightfund.com.au</p>
</section>

<!-- Envelope -->
<section class="piece envelope">
  <svg class="backdrop" viewBox="0 0 828 390" preserveAspectRatio="none" aria-hidden="true">
    <rect width="828" height="390" fill="url(#royal-fill)"/>
    <path d="M0 0 H828 V5 Q450 0 60 150 L0 130 Z" fill="#ffffff" opacity="0.07"/>
  </svg>
  <div class="brand">
    <div class="brand-square"></div>
    <div class="brand-words"><span class="brand-name">brightfund</span><span class="brand-tag">smsf specialists</span></div>
  </div>
  <ul class="envelope-contacts">
    <li>PO Box 318, Harbourview, NT 0870</li>
    <li><svg><use href="#icon-mail"/></svg>info@brightfund.com.au</li>
    <li><svg><use href="#icon-phone"/></svg>3400 5512 28 7</li>
    <li><svg><use href="#icon-phone"/></svg>1300 555 014</li>
    <li><svg><use href="#icon-globe"/></svg>www.brightfund.com.au</li>
  </ul>
</section>

</body>
</html>
```